Brand toolkit and visual identity for an executive search firm

We are an executive search firm / recruitment company that is looking to build a brand toolkit and visual identity, using a newly designed logo.

The next stage of our project is to develop a brand template and visual identity to help us to build a distinct set of fonts/colours/visuals/social medias that we can use to have a uniform style.

I have attached two examples of brand kits that have been designed for two competitor companies. We would like to achieve a similar "brand toolkit"

In terms of our general interests;
- Colour schemes concentrated around greens, black, blue, white are generally attractive
- We like geometric shapes (not 3d ones) but similar to the aesthetics of these two firms:
Example 1
Website: https://www.kestrelvane.com/
LinkedIn: https://www.linkedin.com/company/kestrel-vane/
Example 2
Website: https://www.halbrookeassociates.com/
LinkedIn: https://www.linkedin.com/company/halbrooke-associates/ 

We are looking to achieve a look of elegance/sophistication/exclusivity

Target Market(s)

Our clients are hedge funds, law firms, private equity firms, banks, consulting firms (high end companies)

Industry/Entity Type

Recruitment Agency / Search firm

Colors

Designer to choose colors to be used in the design.

Requirements
Must have
• LinkedIn banner concept, brand style concept, social medial posts concept
Nice to have
• It would be helpful to have some abstract styles (shapes, lines, something geometric) that complements the logo that we can use for backgrounds, social media posts, styling, invoices etc
Should not have
• We don't like old fashioned photos of people / stock photos of executives etc. We prefer abstract shapes/lines/designs and/or cityscapes

```html
<!DOCTYPE html>
<html lang="en">
<head>
<meta charset="utf-8">
<title>Marlow Grant — Social Templates</title>
<link rel="stylesheet" href="https://fonts.googleapis.com/css2?family=Montserrat:wght@700&family=Nunito+Sans:wght@600;700&display=swap">
<style>
  :root {
    --canvas: #ffffff;
    --navy: #0b2b5c;
    --royal: #0d47a8;
    --royal-mid: #1559c4;
    --royal-deep: #0a3a8c;
    --sky: #2aa8e6;
    --cyan: #39c4f2;
    --silver: #c9d3de;
    --white: #ffffff;
    --photo-top: #5d6f86;
    --photo-bottom: #1d3560;
  }
  * { margin: 0; padding: 0; box-sizing: border-box; }
  html, body { width: 1200px; height: 1200px; overflow: hidden; background: var(--canvas); }
  .canvas { position: relative; width: 1200px; height: 1200px; background: var(--canvas); }

  .banner { position: absolute; left: 82px; top: 164px; width: 1035px; height: 257px; overflow: hidden; }
  .banner svg, .post svg { position: absolute; inset: 0; width: 100%; height: 100%; display: block; }

  .headline {
    position: absolute; font-family: "Montserrat", sans-serif; font-weight: 700;
    color: var(--white); text-transform: uppercase; letter-spacing: 1px;
  }
  .quote { position: absolute; font-family: "Nunito Sans", sans-serif; font-weight: 700; color: var(--white); }

  .banner .headline { right: 413px; top: 30px; font-size: 41px; line-height: 44px; text-align: right; }
  .banner .quote { right: 413px; top: 116px; font-size: 18px; line-height: 27px; text-align: right; }
  .banner .brand-name {
    position: absolute; right: 24px; bottom: 26px; font-family: "Nunito Sans", sans-serif;
    font-weight: 700; font-size: 17px; line-height: 19px; color: var(--white); text-align: right;
  }

  .profile-tile {
    position: absolute; left: 211px; top: 365px; width: 102px; height: 102px; background: var(--navy);
    display: flex; align-items: center; justify-content: center; text-align: center;
    font-family: "Nunito Sans", sans-serif; font-weight: 700; font-size: 17px; line-height: 20px; color: var(--white);
  }

  .post { position: absolute; left: 341px; top: 519px; width: 516px; height: 514px; overflow: hidden; }
  .post .brand-name {
    position: absolute; left: 39px; top: 46px; font-family: "Nunito Sans", sans-serif;
    font-weight: 700; font-size: 23px; line-height: 25px; color: var(--white);
  }
  .post .headline { left: 34px; top: 136px; font-size: 56px; line-height: 56px; }
  .post .quote { left: 37px; top: 276px; width: 240px; font-size: 23px; line-height: 30px; }
</style>
</head>
<body>
<div class="canvas">

  <section class="banner">
    <svg viewBox="0 0 850 211" preserveAspectRatio="none">
      <defs>
        <linearGradient id="bannerBase" x1="0" y1="0" x2="1" y2="0">
          <stop offset="0" stop-color="#1352b8"/>
          <stop offset="1" stop-color="#0c419c"/>
        </linearGradient>
        <linearGradient id="cityPhoto" x1="0" y1="0" x2="0" y2="1">
          <stop offset="0" stop-color="var(--photo-top)"/>
          <stop offset="1" stop-color="var(--photo-bottom)"/>
        </linearGradient>
      </defs>
      <rect width="850" height="211" fill="url(#bannerBase)"/>
      <polygon points="143,0 438,211 0,211 0,100" fill="var(--sky)"/>
      <polygon points="143,22 410,211 0,211 0,122" fill="var(--royal-mid)"/>
      <polygon points="143,55 365,211 0,211 0,155" fill="#1048a6"/>
      <polygon points="143,92 313,211 0,211 0,190" fill="var(--royal-deep)"/>
      <polyline points="0,100 143,0 438,211" fill="none" stroke="var(--silver)" stroke-width="1.2"/>
      <g role="img" aria-label="Photograph of glass skyscrapers under a cloudy sky">
        <polygon points="523,0 850,0 688,211 440,211 523,150" fill="url(#cityPhoto)"/>
      </g>
      <polygon points="850,0 850,40 716,211 688,211" fill="var(--cyan)"/>
      <polygon points="850,40 850,211 716,211" fill="var(--royal-mid)"/>
      <line x1="850" y1="40" x2="716" y2="211" stroke="var(--silver)" stroke-width="1.2"/>
    </svg>
    <h2 class="headline">Lorem<br>Ipsum</h2>
    <p class="quote">“Dumy Text Neque porro<br>quisquam est qui dolorem ipsum"</p>
    <div class="brand-name">Marlow<br>Grant</div>
  </section>

  <div class="profile-tile">Marlow<br>Grant</div>

  <section class="post">
    <svg viewBox="0 0 423 422" preserveAspectRatio="none">
      <defs>
        <linearGradient id="postBase" x1="0" y1="0" x2="0" y2="1">
          <stop offset="0" stop-color="#1550b4"/>
          <stop offset="1" stop-color="#1048a6"/>
        </linearGradient>
        <linearGradient id="postCity" x1="0" y1="0" x2="0" y2="1">
          <stop offset="0" stop-color="#33507e"/>
          <stop offset="1" stop-color="#15294d"/>
        </linearGradient>
      </defs>
      <rect width="423" height="422" fill="url(#postBase)"/>
      <g role="img" aria-label="Photograph of tall glass office towers at dusk">
        <polygon points="262,45 423,80 423,160 280,422 262,422" fill="url(#postCity)"/>
      </g>
      <polygon points="95,422 423,250 423,330 260,422" fill="var(--sky)" opacity="0.92"/>
      <polygon points="330,422 423,360 423,422" fill="var(--royal-mid)"/>
      <line x1="95" y1="422" x2="423" y2="250" stroke="var(--silver)" stroke-width="1.2"/>
      <polygon points="0,345 80,422 0,422" fill="var(--cyan)"/>
      <line x1="0" y1="335" x2="90" y2="422" stroke="var(--silver)" stroke-width="1.2"/>
    </svg>
    <div class="brand-name">Marlow<br>Grant</div>
    <h2 class="headline">Lorem<br>Ipsum</h2>
    <p class="quote">“Dumy Text Neque porro quisquam est qui dolorem ipsum"</p>
  </section>

</div>
</body>
</html>
```